Property Auctions with Gareth Whitlow

Podcast cover art 3000px by 3000px. Eye catching for a weekly podcast. The words should read Property Auctions (large font) with Gareth Whitlow (smaller font)

I would like the font and colours to be similar to my book, a copy of which I have attached.

Target Market(s)

New and experienced property investors looking to purchase at a property auction

```html
<!DOCTYPE html>
<html lang="en">
<head>
<meta charset="utf-8">
<title>Property Auctions with Gareth Whitlow – Podcast Cover</title>
<link rel="stylesheet" href="https://fonts.googleapis.com/css2?family=Anton&family=Oswald:wght@600&display=swap">
<style>
  :root {
    --slate-dark: #2a3238;
    --slate-mid: #3a444b;
    --slate-light: #4a545b;
    --gold-bright: #fbf3a0;
    --gold-mid: #dcc766;
    --gold-deep: #a98f3b;
    --gold-edge: #3b2f10;
  }
  html, body {
    margin: 0;
    padding: 0;
    width: 1200px;
    height: 1200px;
    overflow: hidden;
    background: var(--slate-dark);
  }
  .cover {
    display: block;
    width: 1200px;
    height: 1200px;
  }
  .cover-title {
    font-family: "Anton", "Oswald", sans-serif;
    font-size: 262px;
  }
  .cover-host {
    font-family: "Oswald", sans-serif;
    font-weight: 600;
    font-size: 62px;
  }
  .currency-mark {
    font-family: "Anton", sans-serif;
    font-size: 250px;
  }
</style>
</head>
<body>
<svg class="cover" viewBox="0 0 1200 1200" xmlns="http://www.w3.org/2000/svg">
  <defs>
    <radialGradient id="backdrop-glow" cx="50%" cy="50%" r="60%">
      <stop offset="0%" stop-color="var(--slate-light)"/>
      <stop offset="55%" stop-color="var(--slate-mid)"/>
      <stop offset="100%" stop-color="var(--slate-dark)"/>
    </radialGradient>
    <linearGradient id="gold-title" x1="0" y1="0" x2="0" y2="1">
      <stop offset="0%" stop-color="var(--gold-mid)"/>
      <stop offset="45%" stop-color="var(--gold-bright)"/>
      <stop offset="100%" stop-color="var(--gold-deep)"/>
    </linearGradient>
    <linearGradient id="gold-host" x1="0" y1="0" x2="1" y2="0">
      <stop offset="0%" stop-color="var(--gold-deep)"/>
      <stop offset="60%" stop-color="var(--gold-mid)"/>
      <stop offset="100%" stop-color="var(--gold-bright)"/>
    </linearGradient>
    <linearGradient id="gold-symbol" x1="0" y1="1" x2="1" y2="0">
      <stop offset="0%" stop-color="var(--gold-deep)"/>
      <stop offset="100%" stop-color="var(--gold-bright)"/>
    </linearGradient>
    <radialGradient id="house-placeholder" cx="50%" cy="55%" r="55%">
      <stop offset="0%" stop-color="#6b6440" stop-opacity="0.45"/>
      <stop offset="100%" stop-color="var(--slate-mid)" stop-opacity="0"/>
    </radialGradient>
  </defs>

  <rect class="backdrop" width="1200" height="1200" fill="url(#backdrop-glow)"/>

  <g class="cover-title" fill="url(#gold-title)" stroke="var(--gold-edge)" stroke-width="2">
    <text x="71" y="336" textLength="1054" lengthAdjust="spacingAndGlyphs">PROPERTY</text>
    <text x="92" y="571" textLength="1000" lengthAdjust="spacingAndGlyphs">AUCTIONS</text>
  </g>

  <rect class="house-artwork" x="274" y="656" width="652" height="250" fill="url(#house-placeholder)"
        role="img" aria-label="Gold line drawing of a house roofline with small windows"/>

  <text class="currency-mark" x="0" y="0" fill="url(#gold-symbol)"
        transform="translate(120 1110) rotate(25)">£</text>
  <text class="currency-mark" x="0" y="0" fill="url(#gold-symbol)"
        transform="translate(950 1095) rotate(-22)">$</text>

  <text class="cover-host" x="419" y="1119" fill="url(#gold-host)"
        textLength="362" lengthAdjust="spacingAndGlyphs">GARETH WHITLOW</text>
</svg>
</body>
</html>
```